Lani Wellness Clinic Website - this is a website for a medical practice

This is a medical practice and would like my logo to be presented. I have attached a copy of some copy that should give you an idea of what my practice is about. My practice will be seeing Elderaid patients in their homes. No coming to the office for a visit. I listen to my patients and provide individualized care. The name "Lani" means star in Hawaiʻian and want the patient to feel that they are the main focus of my practice.

Target Market(s)

Elderaid patients

Industry/Entity Type

medical

Coding

Coded - Design and coding required

Number of Pages Required

2 page

Font styles to use
Sans Serif

Colors
00AB8E
00BBA5
67D7C9
C6EFE9
E9F9F6

Requirements
Must have
• feeling that I care about each patient and that I will do my very best to keep them as healthy as possible, that the Hawaiʻian culture is represented. Simple and easy to navigate for someone who isnʻt tech savvy. In normal conversational language.
Nice to have
• The elderly in Hawaiʻi are called Kapuna and they are revered. I would like to convey that.
Should not have
• Medical jargon

```html
<!DOCTYPE html>
<html lang="en">
<head>
<meta charset="utf-8">
<title>Lani Wellness Clinic</title>
<link href="https://fonts.googleapis.com/css2?family=Fira+Sans:wght@400;500;600;700&family=Open+Sans:wght@400;600;700&display=swap" rel="stylesheet">
<style>
:root{
  --navy:#1f3d73;
  --navy-dark:#1a2f57;
  --teal:#00ab8e;
  --teal-2:#00bba5;
  --teal-3:#67d7c9;
  --mint:#c6eFe9;
  --mint-2:#e9f9f6;
  --ink:#2b2b2b;
  --muted:#777;
  --light:#f3f4f7;
  --white:#fff;
}
*{box-sizing:border-box;margin:0;padding:0}
html,body{width:1200px;height:4861px;overflow:hidden;background:var(--white)}
body{position:relative;font-family:"Open Sans",sans-serif;color:var(--ink)}
.abs{position:absolute}
h1,h2,h3,.heading{font-family:"Fira Sans",sans-serif}

/* header */
.topbar{left:387px;top:0;width:813px;height:30px;background:var(--navy);display:flex;align-items:center;font-size:11px;font-weight:700;color:var(--white)}
.topbar .item{display:flex;align-items:center;gap:8px;height:100%;padding:0 20px}
.topbar .phone{width:209px;justify-content:center}
.topbar .appt{background:var(--teal);width:234px;justify-content:center;text-transform:uppercase}
.topbar svg{width:14px;height:14px}
.brand{left:145px;top:30px;display:flex;align-items:center;gap:10px}
.brand .dot{width:34px;height:34px;border-radius:50%;background:var(--mint);}
.brand span{font-family:"Fira Sans",sans-serif;font-weight:600;font-size:21px;color:var(--teal);line-height:1.1}
.nav{top:60px;left:396px;display:flex;gap:0;font-size:10px;color:var(--ink)}
.nav a{position:absolute;white-space:nowrap;text-decoration:none;color:var(--ink)}
.btn-outline{left:932px;top:55px;width:117px;height:30px;border:1.5px solid var(--navy);border-radius:3px;font-size:10px;font-weight:600;color:var(--navy);display:flex;align-items:center;justify-content:center;text-transform:uppercase}

/* hero */
.hero{left:0;top:100px;width:1200px;height:645px;background:linear-gradient(120deg,#4b4f57 0%,#7d7a78 35%,#a49a92 55%,#5f6066 80%,#3e4350 100%)}
.hero-shade{left:0;top:100px;width:1200px;height:645px;background:linear-gradient(180deg,rgba(20,25,35,.35),rgba(20,25,35,.5))}
.pill{left:515px;top:302px;width:166px;height:34px;background:var(--navy);color:var(--white);font-size:11px;font-weight:700;display:flex;align-items:center;justify-content:center}
.hero-title{left:200px;top:345px;width:800px;text-align:center;color:var(--white);font-size:62px;font-weight:600;line-height:72px}
.btn-ghost{left:517px;top:519px;width:164px;height:43px;border:1.5px solid var(--white);color:var(--white);font-size:10px;font-weight:700;display:flex;align-items:center;justify-content:center}
.hero-curve{left:0;top:620px;width:1200px;height:130px}

/* about */
.label{font-family:"Open Sans",sans-serif;font-size:12px;font-weight:600;color:var(--navy);text-transform:uppercase;border-bottom:2px solid var(--teal);padding-bottom:4px}
.photo{border-radius:4px}
.star-badge{left:296px;top:1076px;width:102px;height:102px;border-radius:50%;background:var(--white);box-shadow:0 4px 14px rgba(0,0,0,.12);display:flex;align-items:center;justify-content:center}
.star-badge i{width:40px;height:40px;border-radius:50%;background:var(--mint)}
.about-title{left:623px;top:866px;width:520px;font-size:41px;line-height:54px;font-weight:600;color:var(--navy)}
.about-sub{left:623px;top:1000px;font-size:21px;font-weight:500;color:var(--ink);font-family:"Fira Sans",sans-serif}
.about-body{left:623px;top:1047px;width:462px;font-size:12.2px;line-height:21.8px;color:var(--muted)}
.about-body b{color:var(--navy)}
.btn-teal{background:var(--teal);color:var(--white);font-weight:600;display:flex;align-items:center;justify-content:center;gap:10px;border-radius:3px}

/* services */
.services{left:0;top:1455px;width:1200px;height:651px;background:var(--light)}
.sec-title{font-size:40px;font-weight:600;color:var(--navy);text-align:center;width:1200px;left:0}
.svc-img{height:263px;top:1732px}
.svc-icon{width:90px;height:90px;top:1685px;border-radius:50%;background:var(--navy);border:5px solid var(--white);box-shadow:0 0 0 3px var(--teal-2);display:flex;align-items:center;justify-content:center}
.svc-icon svg{width:38px;height:38px}
.svc-label{top:1949px;width:274px;height:95px;background:var(--white);box-shadow:0 6px 18px rgba(0,0,0,.08);display:flex;align-items:center;justify-content:center;font-family:"Fira Sans",sans-serif;font-size:19px;font-weight:500;color:var(--navy)}

/* band */
.band{left:0;top:2106px;width:1200px;height:309px;background:linear-gradient(100deg,#5a4329 0%,#8f6a41 35%,#b08855 55%,#7a5c3d 80%,#4f3a25 100%)}
.band-text{left:200px;top:2214px;width:800px;text-align:center;color:var(--white);font-size:33px;line-height:42px;font-family:"Fira Sans",sans-serif}
.contact-pill{left:351px;top:2381px;width:502px;height:59px;background:var(--white);border-radius:6px;box-shadow:0 6px 18px rgba(0,0,0,.12);display:flex;align-items:center;justify-content:space-around;font-size:16px;color:var(--ink);padding:0 20px}

/* why */
.why-bg{left:0;top:2415px;width:1200px;height:789px;background:linear-gradient(90deg,#e9eef3 0%,#dfe6ee 55%,#b9c4cf 100%)}
.why-photo{left:800px;top:2415px;width:400px;height:789px;background:linear-gradient(180deg,#8d97a3 0%,#c8aa94 40%,#4d6f9c 70%,#3e5f8d 100%)}
.card{background:var(--white);border-radius:4px;box-shadow:0 6px 20px rgba(0,0,0,.07);text-align:center;padding-top:28px}
.card .ic{width:84px;height:84px;border-radius:50%;background:#eef0f3;margin:0 auto;display:flex;align-items:center;justify-content:center}
.card .ic svg{width:38px;height:38px}
.card h3{font-size:21px;font-weight:500;color:var(--navy);margin-top:16px}
.card p{font-size:12.5px;line-height:18px;color:var(--muted);margin:12px auto 0;width:185px}
.card.active{background:var(--navy)}
.card.active h3,.card.active p{color:var(--white)}
.card.active .ic{background:var(--white)}

/* reviews */
.rev-bg{left:0;top:3204px;width:1200px;height:359px;background:linear-gradient(100deg,#3a3f48 0%,#6b6a70 40%,#8c8c92 60%,#4a4f59 100%)}
.rev-shade{left:0;top:3204px;width:1200px;height:359px;background:rgba(15,20,30,.35)}
.rev-card{top:3444px;width:300px;height:326px;background:var(--white);box-shadow:0 8px 22px rgba(0,0,0,.1);padding:40px 40px 0 42px}
.stars{color:#ee7a2d;font-size:17px;letter-spacing:8px}
.rev-card p{font-size:12.5px;line-height:19px;color:var(--muted);margin-top:18px;height:100px}
.rev-card hr{border:0;border-top:1px solid #ddd;margin-top:22px}
.who{display:flex;align-items:center;gap:14px;margin-top:18px}
.who i{width:58px;height:58px;border-radius:50%;background:linear-gradient(160deg,#c9ced6,#7a8796)}
.who b{display:block;font-size:14px;color:#555}
.who small{font-size:12px;color:#888}
.quote{width:52px;height:52px;border-radius:50%;background:var(--teal);display:flex;align-items:center;justify-content:center;top:3480px}
.quote svg{width:26px;height:26px}

/* contact */
.swoosh{left:0;top:4280px;width:1200px;height:160px}
.form-card{left:138px;top:4004px;width:922px;height:459px;background:var(--white);border-radius:12px;box-shadow:0 10px 30px rgba(0,0,0,.1);overflow:hidden}
.form-photo{left:0;top:0;width:464px;height:459px;background:linear-gradient(135deg,#bfc7d2 0%,#a79a8c 45%,#6d7888 100%)}
.field{position:absolute;border:1px solid #cfd3d8;border-radius:3px;font-size:10px;color:#777;padding:8px 8px}

/* footer */
.footer{left:0;top:4463px;width:1200px;height:343px;background:linear-gradient(180deg,#f1f4f8,#e6ebf1)}
.flink{top:4626px;font-size:13px;font-weight:600;color:var(--navy-dark);font-family:"Fira Sans",sans-serif}
.fitem{top:4722px;display:flex;align-items:center;gap:14px}
.fitem .ring{width:56px;height:56px;border-radius:50%;border:2px solid #56617a;display:flex;align-items:center;justify-content:center}
.fitem .ring svg{width:28px;height:28px}
.fitem b{display:block;font-size:13px;color:var(--navy-dark)}
.fitem small{font-size:11px;color:var(--navy-dark);font-weight:600}
.bottombar{left:0;top:4806px;width:1200px;height:55px;background:var(--teal);display:flex;align-items:center;color:var(--white);font-size:12px;font-weight:700}
.social{width:24px;height:24px;border:1.5px solid var(--white);border-radius:3px;top:4819px}
</style>
</head>
<body>

<!-- Header -->
<div class="abs topbar">
  <div class="item phone"><svg viewBox="0 0 24 24" fill="none" stroke="#fff" stroke-width="2"><path d="M5 3h4l2 5-3 2a12 12 0 0 0 6 6l2-3 5 2v4a2 2 0 0 1-2 2A17 17 0 0 1 3 5a2 2 0 0 1 2-2z"/></svg>808-555-0142</div>
  <div class="item appt"><svg viewBox="0 0 24 24" fill="none" stroke="#fff" stroke-width="2"><rect x="3" y="5" width="18" height="14" rx="1"/><path d="M3 6l9 7 9-7"/></svg>Request an appointment</div>
  <div class="item"><svg viewBox="0 0 24 24" fill="none" stroke="#fff" stroke-width="2"><rect x="3" y="5" width="18" height="14" rx="1"/><path d="M3 6l9 7 9-7"/></svg>Fax: 808-555-0178</div>
</div>
<div class="abs brand"><div class="dot"></div><span>Lani Wellness<br>Clinic</span></div>
<nav class="abs nav">
  <a style="left:0;font-weight:700">HOME</a>
  <a style="left:76px">About Us</a>
  <a style="left:151px">Services</a>
  <a style="left:227px">Our team</a>
  <a style="left:312px">Contact Us</a>
</nav>
<div class="abs btn-outline">Contact us</div>

<!-- Hero -->
<div class="abs hero" role="img" aria-label="Photo of a smiling caregiver embracing an elderly patient at home"></div>
<div class="abs hero-shade"></div>
<div class="abs pill">WELCOME</div>
<h1 class="abs hero-title">Bringing Health to<br>Your Home</h1>
<div class="abs btn-ghost">LEARN MORE</div>
<svg class="abs hero-curve" viewBox="0 0 1200 130" preserveAspectRatio="none">
  <path d="M0 40 C300 140 800 110 1200 20 L1200 130 L0 130 Z" fill="#fff"/>
  <path d="M0 40 C300 125 800 100 1200 18 L1200 36 C800 110 300 135 0 50 Z" fill="#00ab8e"/>
  <path d="M0 52 C300 138 800 118 1200 40 L1200 62 C800 128 320 148 0 62 Z" fill="#1f3d73"/>
</svg>

<!-- About -->
<div class="abs label" style="left:623px;top:830px">About Us</div>
<div class="abs photo" style="left:90px;top:943px;width:246px;height:363px;background:linear-gradient(160deg,#a9c3b9,#8a7b6e 60%,#5a5450)" role="img" aria-label="Portrait of a smiling nurse practitioner with a flower in her hair"></div>
<div class="abs photo" style="left:351px;top:898px;width:225px;height:221px;background:linear-gradient(150deg,#d8d2c6,#b59f86 60%,#8a7360)" role="img" aria-label="Photo of a happy elderly couple at home"></div>
<div class="abs photo" style="left:351px;top:1132px;width:225px;height:221px;background:linear-gradient(150deg,#cfd5dc,#9aa6b4 55%,#6e7b8c)" role="img" aria-label="Photo of a caregiver assisting an elderly man"></div>
<div class="abs star-badge"><i></i></div>
<h2 class="abs about-title">Enriching Lives, One Home at a Time</h2>
<div class="abs about-sub">Holistic Care, Heartfelt Connections</div>
<p class="abs about-body">Lani means "star" in Hawaiian and we want our patients to feel that they are the focus in our practice. Lani Wellness Clinic is a leading medical clinic on O'ahu, dedicated to providing exceptional healthcare services to our patients. With a highly skilled and experienced Nurse Practitioner, we are committed to delivering personalized care. Our mission is to ensure the well-being of our patients by offering comprehensive medical services, including primary care, and preventive care. We prioritize patient comfort and convenience by <b>visiting you in your home</b> removing the need to drive to an office. We minimize wait times and offering on-call providers and same-day appointments whenever possible and offer Telehealth appointments for follow-up. Contact us today to experience the highest standard of healthcare.</p>
<div class="abs btn-teal" style="left:623px;top:1330px;width:154px;height:44px;font-size:14px">Learn More <svg width="16" height="16" viewBox="0 0 24 24" fill="none" stroke="#fff" stroke-width="2.5"><path d="M4 12h15M13 6l6 6-6 6"/></svg></div>

<!-- Services -->
<div class="abs services"></div>
<div class="abs label" style="left:553px;top:1534px;text-transform:none;font-weight:400;font-size:11px">Our Services</div>
<h2 class="abs sec-title" style="top:1570px">Our Services</h2>

<div class="abs svc-img" style="left:90px;width:325px;background:linear-gradient(135deg,#cfd8dc,#a8b5b0 50%,#6f8a87)" role="img" aria-label="Photo of a nurse practitioner greeting a senior patient"></div>
<div class="abs svc-img" style="left:440px;width:326px;background:linear-gradient(135deg,#e4e2de,#b9b1a6 50%,#8d8478)" role="img" aria-label="Photo of a senior woman resting at home"></div>
<div class="abs svc-img" style="left:791px;width:326px;background:linear-gradient(135deg,#6c8aa6,#4e7295 50%,#b69c86)" role="img" aria-label="Photo of a caregiver checking a patient's health"></div>

<div class="abs svc-icon" style="left:208px"><svg viewBox="0 0 24 24" fill="#fff"><circle cx="12" cy="4" r="1.6"/><circle cx="17.7" cy="6.3" r="1.6"/><circle cx="20" cy="12" r="1.6"/><circle cx="17.7" cy="17.7" r="1.6"/><circle cx="12" cy="20" r="1.6"/><circle cx="6.3" cy="17.7" r="1.6"/><circle cx="4" cy="12" r="1.6"/><circle cx="6.3" cy="6.3" r="1.6"/></svg></div>
<div class="abs svc-icon" style="left:558px"><svg viewBox="0 0 24 24" fill="none" stroke="#fff" stroke-width="1.8"><path d="M10 13V5a2 2 0 0 1 4 0v6l4 1a2 2 0 0 1 1.5 2.3L18 21H10l-4-5 1.5-1.5L10 16"/><path d="M7 8a5 5 0 0 1 10 0"/></svg></div>
<div class="abs svc-icon" style="left:909px"><svg viewBox="0 0 24 24" fill="#fff"><path d="M12 2l1.5 4h-3zM12 22l-1.5-4h3zM2 12l4-1.5v3zM22 12l-4 1.5v-3z"/><circle cx="12" cy="12" r="2"/><circle cx="6" cy="6" r="1.2"/><circle cx="18" cy="6" r="1.2"/><circle cx="6" cy="18" r="1.2"/><circle cx="18" cy="18" r="1.2"/></svg></div>

<div class="abs svc-label" style="left:117px">Nurse Practitioner</div>
<div class="abs svc-label" style="left:462px">Primary Care</div>
<div class="abs svc-label" style="left:817px">Preventative Care</div>

<!-- 24/7 band -->
<div class="abs band" role="img" aria-label="Photo of caring hands holding an elder's hand"></div>
<div class="abs band-text">We are available 24/7 to cater for your<br>Health needs</div>
<div class="abs contact-pill"><span>808-555-0142</span><span>[or]</span><span>hello@laniwellness.com</span></div>

<!-- Why choose -->
<div class="abs why-bg"></div>
<div class="abs why-photo" role="img" aria-label="Photo of a friendly caregiver standing with arms crossed"></div>
<div class="abs label" style="left:538px;top:2473px;color:var(--teal);border:0;font-size:11px">Why Choose Us</div>
<h2 class="abs sec-title" style="top:2510px;width:800px">Why Choose Us</h2>

<div class="abs card" style="left:98px;top:2608px;width:234px;height:260px">
  <div class="ic"><svg viewBox="0 0 24 24" fill="none" stroke="#00ab8e" stroke-width="2"><path d="M5 13a7 7 0 0 1 14 0v3h-3v-4M5 13v3h3v-4"/><circle cx="12" cy="13" r="3"/></svg></div>
  <h3>Quality Services</h3><p>Encompasses excellence, safety, and patient-centered care for optimal well-being</p></div>
<div class="abs card active" style="left:355px;top:2608px;width:232px;height:260px">
  <div class="ic"><svg viewBox="0 0 24 24" fill="none" stroke="#00ab8e" stroke-width="2"><circle cx="12" cy="12" r="8"/><circle cx="12" cy="12" r="4"/></svg></div>
  <h3>Expertise</h3><p>Advanced knowledge, skill, and proficiency in medical practices.</p></div>
<div class="abs card" style="left:611px;top:2608px;width:234px;height:260px">
  <div class="ic"><svg viewBox="0 0 24 24" fill="none" stroke="#00ab8e" stroke-width="2"><circle cx="12" cy="4.5" r="2"/><path d="M5 9h14M12 9v5l-4 7M12 14l4 7"/></svg></div>
  <h3>Client-centric</h3><p>Prioritizes individual needs, ensuring a positive patient experience.</p></div>
<div class="abs card" style="left:98px;top:2893px;width:234px;height:260px">
  <div class="ic"><svg viewBox="0 0 24 24" fill="none" stroke="#00ab8e" stroke-width="2"><circle cx="7" cy="8" r="2.5"/><path d="M2 17a5 5 0 0 1 10 0M14 8h8M14 12h8M14 16h6"/></svg></div>
  <h3>Personalized</h3><p>Tailored to the individual, addressing unique needs with attention and care</p></div>
<div class="abs card" style="left:355px;top:2893px;width:232px;height:260px">
  <div class="ic"><svg viewBox="0 0 24 24" fill="none" stroke="#00ab8e" stroke-width="2"><path d="M4 20v-4M8 20v-7M12 20v-10"/><circle cx="17" cy="4" r="2"/><path d="M17 7v13M14 11h6"/></svg></div>
  <h3>Professional</h3><p>Ethics, and competence define our professional standard.</p></div>
<div class="abs card" style="left:611px;top:2893px;width:234px;height:260px">
  <div class="ic"><svg viewBox="0 0 24 24" fill="none" stroke="#00ab8e" stroke-width="2"><rect x="3" y="3" width="6" height="6"/><rect x="15" y="3" width="6" height="6"/><rect x="3" y="15" width="6" height="6"/><rect x="15" y="15" width="6" height="6"/><path d="M9 6h6M18 9v6M9 18h6"/></svg></div>
  <h3>Proven Record</h3><p>A consistent history of positive outcomes, and patient satisfaction.</p></div>

<!-- Reviews -->
<div class="abs rev-bg" role="img" aria-label="Photo of a doctor talking with a senior patient"></div>
<div class="abs rev-shade"></div>
<div class="abs label" style="left:547px;top:3296px;color:#fff;border-color:#fff;font-size:11px">Testimonials</div>
<h2 class="abs sec-title" style="top:3335px;color:#fff">Client Reviews</h2>

<div class="abs rev-card" style="left:111px"><div class="stars">★★★★★</div><p>Exceptional home healthcare service! Compassionate caregivers, personalized, and peace of mind for our family. Thank you for the top-notch care</p><hr><div class="who"><i></i><div><b>Malia Kahale</b><small>Hawaii</small></div></div></div>
<div class="abs rev-card" style="left:462px"><div class="stars">★★★★★</div><p>Grateful for the outstanding home healthcare service! Dedicated team, prompt and compassionate care. A reliable choice for tailored support, comfort to our home.</p><hr><div class="who"><i></i><div><b>Malia Kahale</b><small>Hawaii</small></div></div></div>
<div class="abs rev-card" style="left:806px"><div class="stars">★★★★★</div><p>Outstanding home healthcare service! Compassionate caregivers, and reliable. Our family's health and happiness are in excellent hands.</p><hr><div class="who"><i></i><div><b>Malia Kahale</b><small>Hawaii</small></div></div></div>

<div class="abs quote" style="left:84px"><svg viewBox="0 0 24 24" fill="#fff"><path d="M3 11c0-4 2-6 5-7l1 2c-2 1-3 2-3 4h3v7H3zM13 11c0-4 2-6 5-7l1 2c-2 1-3 2-3 4h3v7h-6z"/></svg></div>
<div class="abs quote" style="left:435px"><svg viewBox="0 0 24 24" fill="#fff"><path d="M3 11c0-4 2-6 5-7l1 2c-2 1-3 2-3 4h3v7H3zM13 11c0-4 2-6 5-7l1 2c-2 1-3 2-3 4h3v7h-6z"/></svg></div>
<div class="abs quote" style="left:779px"><svg viewBox="0 0 24 24" fill="#fff"><path d="M3 11c0-4 2-6 5-7l1 2c-2 1-3 2-3 4h3v7H3zM13 11c0-4 2-6 5-7l1 2c-2 1-3 2-3 4h3v7h-6z"/></svg></div>

<!-- Contact -->
<div class="abs label" style="left:553px;top:3853px;color:var(--teal);font-size:11px">Contact Us</div>
<h2 class="abs sec-title" style="top:3890px">Get in touch with us</h2>
<div class="abs footer"></div>
<svg class="abs swoosh" viewBox="0 0 1200 160" preserveAspectRatio="none">
  <path d="M0 30 C300 10 900 150 1200 40 L1200 70 C900 170 300 40 0 60 Z" fill="#1f3d73"/>
  <path d="M0 62 C300 45 900 175 1200 75 L1200 95 C900 190 300 70 0 82 Z" fill="#00ab8e"/>
</svg>
<div class="abs form-card">
  <div class="abs form-photo" role="img" aria-label="Photo of a caregiver comforting a senior woman in a headscarf"></div>
  <div class="abs" style="left:516px;top:40px;width:52px;height:52px;border-radius:50%;background:var(--mint)"></div>
  <div class="abs" style="left:511px;top:112px;font-size:28px;color:var(--navy);font-family:'Fira Sans',sans-serif">Please fill out the form</div>
  <div class="field" style="left:511px;top:172px;width:359px;height:34px">Name</div>
  <div class="field" style="left:511px;top:225px;width:172px;height:34px">Phone</div>
  <div class="field" style="left:698px;top:225px;width:172px;height:34px">Email</div>
  <div class="field" style="left:511px;top:278px;width:359px;height:68px">Message</div>
  <div class="abs btn-teal" style="left:511px;top:363px;width:359px;height:37px;font-size:13px">Send</div>
</div>

<!-- Footer -->
<div class="abs" style="left:0;top:4540px;width:1200px;text-align:center;font-family:'Fira Sans',sans-serif;font-size:28px;font-weight:500;color:#56617a">Lani Wellness Clinic</div>
<div class="abs flink" style="left:353px">HOME</div>
<div class="abs flink" style="left:445px">SERVICES</div>
<div class="abs flink" style="left:550px">ABOUT US</div>
<div class="abs flink" style="left:670px">TESTIMONIALS</div>
<div class="abs flink" style="left:821px">BLOG</div>
<div class="abs" style="left:141px;top:4676px;width:918px;height:1px;background:#c7ced8"></div>
<div class="abs" style="left:430px;top:4710px;width:1px;height:68px;background:#9aa3b2"></div>
<div class="abs" style="left:749px;top:4710px;width:1px;height:68px;background:#9aa3b2"></div>
<div class="abs fitem" style="left:172px"><div class="ring"><svg viewBox="0 0 24 24" fill="none" stroke="#56617a" stroke-width="1.6"><circle cx="12" cy="12" r="9"/><path d="M3 12h18M12 3c3 3 3 15 0 18M12 3c-3 3-3 15 0 18"/></svg></div><div><b>FAX</b><small>808-555-0178</small></div></div>
<div class="abs fitem" style="left:508px"><div class="ring"><svg viewBox="0 0 24 24" fill="none" stroke="#56617a" stroke-width="1.6"><rect x="7" y="3" width="10" height="18" rx="2"/><path d="M11 18h2"/></svg></div><div><b>PHONE</b><small>808-555-0142</small></div></div>
<div class="abs fitem" style="left:827px"><div class="ring"><svg viewBox="0 0 24 24" fill="none" stroke="#56617a" stroke-width="1.6"><rect x="4" y="6" width="16" height="12" rx="1"/><path d="M4 7l8 6 8-6"/></svg></div><div><b>EMAIL</b><small>care@laniwellness.com</small></div></div>

<div class="abs bottombar"><span style="margin-left:147px">Lani Wellness Clinic</span></div>
<div class="abs social" style="left:934px"></div>
<div class="abs social" style="left:968px"></div>
<div class="abs social" style="left:1001px"></div>
<div class="abs social" style="left:1034px"></div>

</body>
</html>
```